Cyber Security firm working in the Financial Services sector needs a brochure

We need a brochure covering our products and offerings. We work exclusively with Independent Broker Dealers, their Reps and RIAs in the US. We help them keep their computers secure and compliant with applicable regulations and policies. Have attached samples of our logo an descriptions of our products and services.

Financial Institutions and Financial Advisors

Financial Service

```html
<!DOCTYPE html>
<html lang="en">
<head>
<meta charset="utf-8">
<title>Services Brochure – Ledgerguard Security</title>
<link href="https://fonts.googleapis.com/css2?family=Roboto+Condensed:wght@700&family=Arimo:wght@400&display=swap" rel="stylesheet">
<style>
  :root {
    --canvas: #e9ecf0;
    --page: #ffffff;
    --page-tint: #d6ebfa;
    --band-dark: #1d4f9e;
    --band-light: #4cc3ee;
    --heading: #1f3f95;
    --body: #1b2740;
    --icon: #8c8c8c;
  }
  html, body { margin: 0; padding: 0; overflow: hidden; }
  body {
    width: 1200px; height: 1200px;
    background: var(--canvas);
    position: relative;
  }
  .brochure-page {
    position: absolute; left: 150px; top: 15px;
    width: 900px; height: 1170px;
    background: linear-gradient(160deg, var(--page) 0%, #f3f9fe 35%, var(--page-tint) 70%, #bfe0f7 100%);
    box-shadow: 0 6px 24px rgba(0,0,0,.25);
    overflow: hidden;
  }
  .band { position: absolute; left: 0; width: 900px; }
  .band--top { top: 0; height: 40px; }
  .band--bottom { bottom: 0; height: 44px; }
  .service {
    position: absolute; left: 180px; width: 682px;
  }
  .service h2 {
    margin: 0 0 8px;
    font-family: "Roboto Condensed", "Arial Narrow", sans-serif;
    font-weight: 700; font-size: 19px; color: var(--heading);
    letter-spacing: .1px;
  }
  .service p {
    margin: 0 0 9px;
    font-family: "Arimo", Arial, sans-serif;
    font-size: 13.3px; line-height: 17.2px;
    color: var(--body); text-align: justify;
    letter-spacing: -.15px;
  }
  .icon { position: absolute; left: 38px; }
  .icon svg { display: block; }
  .icon--placeholder {
    background: linear-gradient(180deg, #b9b9b9, #9a9a9a);
    border-radius: 8px;
  }
</style>
</head>
<body>
<main class="brochure-page">
  <svg class="band band--top" viewBox="0 0 900 40" preserveAspectRatio="none" aria-hidden="true">
    <defs>
      <linearGradient id="bandTop" x1="0" x2="1">
        <stop offset="0" stop-color="#ffffff" stop-opacity="0"/>
        <stop offset=".35" stop-color="var(--band-light)"/>
        <stop offset="1" stop-color="var(--band-dark)"/>
      </linearGradient>
    </defs>
    <polygon points="0,0 900,0 900,38 0,4" fill="url(#bandTop)"/>
  </svg>

  <!-- Broker dealer -->
  <div class="icon icon--placeholder" style="top:40px;width:100px;height:100px" role="img" aria-label="Line illustration of an advisor beside a security shield"></div>
  <section class="service" style="top:38px">
    <h2>Configure for Broker Dealer security requirements</h2>
    <p>Encrypt the Drive | Set password Policy | Apply all Operating System patches | Set computer for Auto-update of all products where possible (if not subscribing to our Managed Software Patching service) | Install default Anti-Virus software and configure to policy requirements (if not subscribing to our Managed Anti-Virus service)</p>
  </section>

  <!-- Functionality -->
  <div class="icon" style="top:153px">
    <svg width="118" height="76" viewBox="0 0 118 76" aria-hidden="true">
      <rect x="3" y="3" width="110" height="56" rx="3" fill="none" stroke="var(--icon)" stroke-width="4"/>
      <path d="M20 30 c0-8 10-8 12-2 c2-6 12-6 12 2 c0 7-12 14-12 14 s-12-7-12-14z" fill="#bdbdbd"/>
      <polyline points="44,34 58,34 66,18 76,48 84,30 104,30" fill="none" stroke="#bdbdbd" stroke-width="2"/>
      <rect x="48" y="59" width="20" height="8" fill="var(--icon)"/>
      <rect x="36" y="67" width="44" height="6" fill="var(--icon)"/>
    </svg>
  </div>
  <section class="service" style="top:145px">
    <h2>Configure for functionality</h2>
    <p>Remove any unneeded software | Configure browsers to function most reliably with BD sites | Remove any unneeded Browser Plug-ins or Tool Bars | Install Kava Runtime (as required) | Install Folio Reader | Install Deskwork Office if needed - We can provide Office for $199</p>
  </section>

  <section class="service" style="top:236px">
    <h2>Safety</h2>
    <p>Create a System Image to an external encrypted drive | Create Encryption Recovery media and keys if applicable</p>
  </section>

  <!-- General support -->
  <div class="icon" style="top:335px">
    <svg width="135" height="102" viewBox="0 0 135 102" aria-hidden="true">
      <rect x="10" y="12" width="112" height="74" rx="3" fill="none" stroke="var(--icon)" stroke-width="5"/>
      <rect x="0" y="88" width="135" height="9" rx="4" fill="var(--icon)"/>
      <g fill="var(--icon)">
        <circle cx="90" cy="38" r="20"/>
        <circle cx="45" cy="62" r="15"/>
        <circle cx="49" cy="18" r="11"/>
      </g>
      <g fill="#fff">
        <circle cx="90" cy="38" r="9"/>
        <circle cx="45" cy="62" r="6"/>
        <circle cx="49" cy="18" r="5"/>
      </g>
      <g stroke="var(--icon)" stroke-width="7">
        <line x1="90" y1="10" x2="90" y2="66"/><line x1="62" y1="38" x2="118" y2="38"/>
        <line x1="70" y1="18" x2="110" y2="58"/><line x1="70" y1="58" x2="110" y2="18"/>
        <line x1="45" y1="43" x2="45" y2="81"/><line x1="26" y1="62" x2="64" y2="62"/>
        <line x1="49" y1="4" x2="49" y2="32"/><line x1="35" y1="18" x2="63" y2="18"/>
      </g>
      <circle cx="90" cy="38" r="8" fill="#fff"/><circle cx="45" cy="62" r="6" fill="#fff"/><circle cx="49" cy="18" r="4" fill="#fff"/>
    </svg>
  </div>
  <section class="service" style="top:307px">
    <h2>General Computer Support</h2>
    <p>Ledgerguard Security has a long history of working with thousands of Independent Financial Advisors and Broker Dealers across the country. Because of this we have a lot of experience in supporting their technology needs. A benefit of this is we not only understand the technology but also the special needs of the financial services industry. All our technicians are US based, have years of industry experience and must pass a rigorous background check. We also understand your security requirements and will execute appropriate non-disclosure agreements to help you insure your information remains private. We've found we can resolve most software and configuration issues remotely. Our rates are $95 per hour.</p>
  </section>

  <!-- Training -->
  <div class="icon" style="top:573px">
    <svg width="128" height="102" viewBox="0 0 128 102" aria-hidden="true">
      <rect x="3" y="3" width="122" height="76" rx="3" fill="none" stroke="var(--icon)" stroke-width="5"/>
      <rect x="54" y="79" width="20" height="10" fill="var(--icon)"/>
      <rect x="32" y="89" width="64" height="8" fill="var(--icon)"/>
      <path d="M64 18 l20 6 v16 c0 14-10 22-20 26 c-10-4-20-12-20-26 v-16z" fill="var(--icon)"/>
      <path d="M64 24 v36 c-6-3-14-9-14-20 v-12z" fill="#fff"/>
      <path d="M64 42 h14 c-1 8-7 14-14 18z" fill="#fff"/>
    </svg>
  </div>
  <section class="service" style="top:467px">
    <h2>Security Awareness Training</h2>
    <p>Security Awareness Training is a critical component of a comprehensive cyber security program. Because the cyber security environment is continuously changing, it is our experience that a multi-level approach is most effective in providing timely, actionable information as well as a firm grasp of critical security principals and requirements.</p>
    <p>Our first level is a targeted, electronic delivery of mini-training modules, typically taking no longer than 10 minutes to complete, every 4-6 weeks. These short, topical modules are designed to highlight current attacks and the appropriate response to the illustrated threat. The attacks are explained in an easy-to-understand format with the amount of technical jargon kept to the bare minimum. Each module presents several multiple choice questions to insure the respondent has a firm grasp of the topic. The continuous, “drip” nature of this timely information is important in keeping security top-of-mind.</p>
    <p>Our second level provides periodic phishing emails. The emails consist of both general phishing emails, spear phishing, as well as very targeted “whaling” types of email. Anyone found susceptible to opening specially crafted attachments or links will be immediately taken to an on-line refresher course on how to spot fraudulent emails. $25 per user per year.</p>
  </section>

  <!-- Blocking -->
  <div class="icon" style="top:798px;left:64px">
    <svg width="86" height="96" viewBox="0 0 86 96" aria-hidden="true">
      <path d="M43 2 l40 12 v30 c0 26-20 44-40 50 c-20-6-40-24-40-50 v-30z" fill="var(--icon)"/>
      <g fill="#fff">
        <rect x="24" y="28" width="8" height="28" rx="4"/>
        <rect x="33" y="20" width="8" height="34" rx="4"/>
        <rect x="42" y="20" width="8" height="34" rx="4"/>
        <rect x="51" y="26" width="8" height="30" rx="4"/>
        <path d="M24 48 h35 v10 c0 12-8 18-17 18 c-8 0-12-4-16-12 l-10-14 c-2-4 4-7 7-3z"/>
      </g>
    </svg>
  </div>
  <section class="service" style="top:776px">
    <h2>Internet Blocking and Filtering</h2>
    <p>Comprehensive security for your network through award-winning phishing, botnet and malware site protection. Our web filtering service delivers network security services through the DNS layer blocking known malicious or infected sites from resolving on your network. This also allows you to block specific web sites and also broad categories of content from being accessed from your locations. A couple of examples might be Gambling and Pornography. $3.50 per month per device.</p>
  </section>

  <!-- Firewall -->
  <div class="icon" style="top:918px;left:60px">
    <svg width="92" height="100" viewBox="0 0 92 100" aria-hidden="true">
      <path d="M46 2 l42 14 v28 c0 28-22 48-42 54 c-20-6-42-26-42-54 v-28z" fill="var(--icon)"/>
      <path d="M46 28 c10 12 18 20 18 32 c0 11-8 18-18 18 s-18-7-18-18 c0-8 5-12 8-16 c0 6 3 9 6 9 c-2-9 1-17 4-25z" fill="#fff"/>
      <path d="M46 56 c5 5 8 8 8 12 c0 5-4 8-8 8 s-8-3-8-8 c0-4 4-7 8-12z" fill="var(--icon)"/>
    </svg>
  </div>
  <section class="service" style="top:904px">
    <h2>Firewall Sales</h2>
    <p>We provide pre-purchase consulting, configuration and support for business grade firewalls. We will help you spec an appropriate firewall, determine if VPN access is needed as well as any dedicated guest Wireless Access. The most suitable device for your location as well as any satellite locations is dependent on organization size and complexity. Prices starting at $750.</p>
  </section>

  <!-- Monitoring -->
  <div class="icon" style="top:1028px;left:66px">
    <svg width="80" height="108" viewBox="0 0 80 108" aria-hidden="true">
      <circle cx="40" cy="34" r="32" fill="var(--icon)"/>
      <circle cx="40" cy="34" r="20" fill="#fff"/>
      <circle cx="40" cy="34" r="13" fill="var(--icon)"/>
      <circle cx="40" cy="34" r="6" fill="#fff"/>
      <path d="M34 66 h12 l-2 12 l26 22 l-5 6 l-25-20 l-25 20 l-5-6 l26-22z" fill="var(--icon)"/>
    </svg>
  </div>
  <section class="service" style="top:1014px">
    <h2>Public IP Monitoring</h2>
    <p>Knowing what the world sees of your front door to the internet is important. Our Public IP Monitoring scans your static IP address daily looking for inappropriate ports being made available over the internet. If we find your device has changes made we contact you to verify the changes were intentional and explain the ramifications of the changes. We don't want your network exposed because the Tech installing your new copier decided to open up a number of ports on your firewall. $100 per year per IP address.</p>
  </section>

  <svg class="band band--bottom" viewBox="0 0 900 44" preserveAspectRatio="none" aria-hidden="true">
    <defs>
      <linearGradient id="bandBottom" x1="0" x2="1">
        <stop offset="0" stop-color="var(--band-dark)"/>
        <stop offset=".6" stop-color="var(--band-light)"/>
        <stop offset="1" stop-color="#ffffff" stop-opacity="0"/>
      </linearGradient>
    </defs>
    <polygon points="0,4 900,40 900,44 0,44" fill="url(#bandBottom)"/>
  </svg>
</main>
</body>
</html>
```